Holloway Arms Retail Store Simple Website to attract customers and help existing customers.

I want to keep the site simple and to intergrate our existing logo. We dont need any kind of online checkout system but we would like to link to our auctions.

www.hollowayarms-example.com is our existing site and we are not very fond of it. But it contains the majority of the information we want displayed. I know Bidmarket-example.com offers some much better ways to display auctions right from within your own webpage so that could be interesting.

Target Market(s)

Firearms buyers, sellers, traders, consigners.

Industry/Entity Type

Gun

Coding

Coded - Design and coding required

Number of Pages Required

1 page

Colors

Designer to choose colors to be used in the design.

Requirements
Must have
• Simple and not over complicated or busy.
Nice to have
• HTML that can be modified without special tools. In case we need to make a simple change such as business hours we can do that without having to rehire someone.
Should not have
• Checkout or other online buying tools and or checkout. We don't do online sales except at online auction.

```html
<!DOCTYPE html>
<html lang="en">
<head>
<meta charset="utf-8">
<title>Holloway Arms</title>
<link href="https://fonts.googleapis.com/css2?family=Montserrat:wght@400;500;600;700&family=Open+Sans:wght@400;600;700&display=swap" rel="stylesheet">
<style>
:root{
  --red:#c00d0d;
  --red-dark:#a40a0a;
  --ink:#222;
  --text:#666;
  --muted:#888;
  --panel:#f2f2f2;
  --line:#e2e2e2;
  --white:#fff;
  --footer:#161616;
  --footer-line:#333;
  --footer-field:#2a2a2a;
  --orange:#d9820d;
  --tan:#c9a46a;
}
*{box-sizing:border-box;margin:0;padding:0}
html,body{width:1200px;height:2242px;overflow:hidden}
body{font-family:"Open Sans",sans-serif;color:var(--text);background:var(--white);position:relative}
.abs{position:absolute}

/* header */
.topbar{position:absolute;left:0;top:0;width:1200px;height:90px;background:var(--white)}
.brand{position:absolute;left:86px;top:20px;width:134px;height:66px;background:var(--tan);display:flex;align-items:center;justify-content:center;font-family:"Montserrat",sans-serif;font-weight:700;font-size:14px;color:#3b2a14;text-align:center;line-height:1.2}
.info{position:absolute;top:26px;display:flex;gap:10px;align-items:flex-start;font-size:12px;line-height:19px;color:var(--ink);white-space:nowrap}
.info b{font-family:"Montserrat",sans-serif;font-weight:600;font-size:13px}
.info span{color:var(--muted)}
.info svg{flex:none;margin-top:3px}
.nav{position:absolute;left:0;top:90px;width:1200px;height:45px;background:var(--red);border-bottom:2px solid var(--red-dark)}
.nav ul{list-style:none;display:flex;gap:24px;position:absolute;left:242px;top:0;height:45px;align-items:center}
.nav a{font-family:"Montserrat",sans-serif;font-weight:600;font-size:12px;color:var(--white);text-decoration:none;text-transform:uppercase;position:relative}
.nav a.active::after{content:"";position:absolute;left:0;right:0;bottom:-9px;height:2px;background:var(--white)}

/* hero */
.hero{position:absolute;left:0;top:135px;width:1200px;height:316px;background:linear-gradient(90deg,#6e3c37 0%,#8a5149 35%,#b78a74 65%,#d9c4b4 100%)}
.hero h1{position:absolute;left:87px;top:100px;font-family:"Montserrat",sans-serif;font-weight:700;font-size:32px;line-height:52px;color:var(--white)}

/* intro */
.intro{position:absolute;left:93px;top:508px;width:670px}
.intro h2{font-family:"Montserrat",sans-serif;font-weight:600;font-size:28px;color:var(--ink);margin-bottom:20px}
.intro p{font-size:13.5px;line-height:22.5px;color:var(--text)}
.intro p+p{margin-top:22px}

/* showcase */
.showcase{position:absolute;left:91px;top:820px;width:671px;height:706px;background:var(--panel)}
.showcase h3{position:absolute;left:18px;top:24px;font-family:"Montserrat",sans-serif;font-weight:500;font-size:17px;color:#444}
.card{position:absolute;width:181px;height:265px;background:var(--white)}
.card .thumb{position:absolute;left:8px;top:8px;width:165px;height:116px}
.card .name{position:absolute;left:16px;top:136px;width:150px;font-size:12px;line-height:18px;color:#555}
.card .foot{position:absolute;left:0;bottom:0;width:181px;height:66px;border-top:1px solid var(--line);font-size:12px;color:#555}
.card .left{position:absolute;left:14px;top:22px}
.card .right{position:absolute;right:22px;top:14px;text-align:right;line-height:18px}
.featured-bg{position:absolute;width:197px;height:274px;background:#dcdcdc;border-radius:4px}
.card.featured .thumb{top:0;left:0;width:181px;height:122px}
.badge{position:absolute;left:6px;top:22px;background:var(--red);color:var(--white);padding:2px 14px;font-size:12px}
.warm{background:linear-gradient(135deg,#d6a987,#8d5a48 70%,#5e3b30)}
.dark{background:linear-gradient(135deg,#3a3a3a,#1b1b1b)}
.cool{background:linear-gradient(135deg,#58606a,#2b3138)}

/* sidebar */
.auction{position:absolute;left:802px;width:308px;height:334px;background:var(--panel)}
.auction h4{position:absolute;left:17px;top:23px;font-family:"Montserrat",sans-serif;font-weight:500;font-size:15px;color:#444}
.auction .more{position:absolute;right:14px;top:24px;font-size:12px;color:var(--red);display:flex;align-items:center;gap:6px}
.auction .thumb{position:absolute;left:17px;top:56px;width:276px;height:107px}
.auction .title{position:absolute;left:17px;top:181px;font-size:11.5px;font-weight:700;color:#444}
.auction .sub{position:absolute;left:17px;top:200px;font-size:11.5px;color:#555}
.auction .box{position:absolute;left:17px;top:247px;width:276px;height:60px;background:var(--white);border:1px solid #ddd;font-size:12px;color:#555}
.auction .box .left{position:absolute;left:12px;top:20px}
.auction .box .right{position:absolute;right:14px;top:10px;text-align:right;line-height:19px}
.gold{background:linear-gradient(135deg,#c9b59b,#9c8a74 50%,#7a5c45)}
.steel{background:linear-gradient(135deg,#b7b2a9,#6c6a66 60%,#4a4845)}

.promo{position:absolute;left:807px;top:865px;width:275px;height:229px;background:var(--red);border:2px solid #8f0c0c;overflow:hidden;text-decoration:none}
.promo .head{position:absolute;left:0;top:4px;width:100%;text-align:center;font-family:"Montserrat",sans-serif;font-weight:700;font-size:19px;line-height:24px;color:var(--white)}
.promo .photo{position:absolute;left:0;top:62px;width:130px;height:132px;background:linear-gradient(135deg,#b04040,#5c2a2a)}
.promo .panel{position:absolute;left:130px;top:62px;width:141px;height:132px;background:var(--white)}
.promo .org{position:absolute;left:10px;top:12px;font-family:"Montserrat",sans-serif;font-weight:700;font-size:15px;color:#222;line-height:18px}
.promo .seal{position:absolute;left:42px;top:54px;width:40px;height:30px;border:2px solid #222}
.promo .join{position:absolute;left:8px;top:92px;font-family:"Montserrat",sans-serif;font-weight:700;font-size:16px;color:var(--red)}
.promo .url{position:absolute;left:4px;top:115px;font-size:6.5px;font-weight:700;color:#222;white-space:nowrap}
.promo .cta{position:absolute;left:0;bottom:0;width:100%;height:31px;text-align:center;font-family:"Montserrat",sans-serif;font-weight:700;font-size:20px;line-height:31px;color:var(--white)}

/* brands */
.brands{position:absolute;left:100px;top:1600px;width:1000px;height:72px;display:flex;justify-content:space-between;align-items:center}
.brands span{font-family:"Montserrat",sans-serif;font-weight:700;font-size:13px;color:#333;display:flex;align-items:center;gap:6px}
.brands i{display:inline-block;width:14px;height:14px;border-radius:50%;background:#333}

/* footer */
.footer{position:absolute;left:0;top:1721px;width:1200px;height:521px;background:var(--footer);color:#ccc}
.footer .brand{left:124px;top:15px;width:96px;height:60px;font-size:12px}
.social{position:absolute;display:flex;gap:8px}
.social i{display:block;width:26px;height:26px;border-radius:50%;border:1px solid #666}
.footer .rule{position:absolute;left:112px;top:89px;width:1003px;height:1px;background:var(--footer-line)}
.col{position:absolute;top:163px}
.col h5{font-family:"Montserrat",sans-serif;font-weight:500;font-size:15px;color:var(--white);text-transform:uppercase;margin-bottom:33px}
.col h5.strong{font-weight:700}
.contact{width:240px}
.contact li{list-style:none;display:flex;gap:14px;align-items:flex-start;font-size:13px;line-height:20px;color:#ddd;margin-bottom:23px}
.contact svg{flex:none;margin-top:3px}
.news li{list-style:none;margin-bottom:24px}
.news b{display:block;font-weight:400;font-size:13px;color:#eee}
.news em{display:block;font-size:10px;color:#999}
.about li{list-style:none;font-family:"Montserrat",sans-serif;font-weight:600;font-size:10px;color:#ddd;line-height:22.3px;text-transform:uppercase}
.field{width:215px;height:36px;background:var(--footer-field);margin-bottom:9px;font-size:11px;color:#ddd;padding:10px 15px;text-transform:uppercase}
.field.area{height:72px;text-transform:none}
.submit{width:114px;height:36px;background:var(--orange);color:var(--white);font-family:"Montserrat",sans-serif;font-weight:700;font-size:13px;line-height:36px;text-align:center;margin-top:11px}
.copyright{position:absolute;left:0;top:470px;width:1200px;text-align:center;font-size:12px;color:#aaa}
</style>
</head>
<body>

<header class="topbar">
  <div class="brand">Holloway Arms</div>
  <div class="info" style="left:540px">
    <svg width="22" height="22" viewBox="0 0 24 24" fill="none" stroke="#999" stroke-width="1.5"><path d="M5 3h4l2 5-2.5 1.5a11 11 0 0 0 6 6L16 13l5 2v4a2 2 0 0 1-2 2A16 16 0 0 1 3 5a2 2 0 0 1 2-2z"/></svg>
    <div><b>720-555-0186</b><br><span>info@hollowayarms-example.com</span></div>
  </div>
  <div class="info" style="left:772px">
    <svg width="20" height="26" viewBox="0 0 20 26" fill="none" stroke="#999" stroke-width="1.5"><path d="M10 25S2 15 2 9a8 8 0 0 1 16 0c0 6-8 16-8 16z"/><circle cx="10" cy="9" r="3"/></svg>
    <div><b>2210 Quarry Ave, STE A</b><br><span>Pine Hollow, CO 80199</span></div>
  </div>
  <div class="info" style="left:986px">
    <svg width="22" height="22" viewBox="0 0 24 24" fill="none" stroke="#999" stroke-width="1.5"><circle cx="12" cy="12" r="10"/><path d="M12 6v6l4 2"/></svg>
    <div><b>7:30 AM - 7:30 PM</b><br><span>Monday to Saturday</span></div>
  </div>
</header>

<nav class="nav">
  <ul>
    <li><a class="active" href="#">Home</a></li>
    <li><a href="#">Tactical/LE</a></li>
    <li><a href="#">Hunting</a></li>
    <li><a href="#">Personal Defense</a></li>
    <li><a href="#">Cowboy</a></li>
    <li><a href="#">Consignments</a></li>
    <li><a href="#">Accessories</a></li>
    <li><a href="#">About Us</a></li>
    <li><a href="#">Find Us</a></li>
  </ul>
</nav>

<section class="hero" role="img" aria-label="Shooters at an outdoor range firing handguns">
  <h1>Guns, Ammo, Hunting,<br>Tactical &amp; Personal Defense</h1>
</section>

<section class="intro">
  <h2>Why Choose Holloway Arms</h2>
  <p>Holloway Arms is open and offering firearms, ammunition, holsters, cleaning, safety gear, tactical supplies and support. Come on into our retail store nestled in a small town of Pine Hollow just minutes from Ridgefield / Stone Bluff<br>Our service and attention to you are what you would expect of a professional gun shop.</p>
  <p>Holloway Arms caters to those requiring quality firearms for hunting, shooting , home and personal defense and tactical/target solutions We try to tailor our product line to meet the needs of our customers. If there is something you want, just let us know and we will be happy to help.</p>
  <p>Trade or purchase of your firearm will always be considered.</p>
</section>

<section class="showcase">
  <h3>Showcase Items</h3>

  <div class="card" style="left:25px;top:70px">
    <div class="thumb warm" role="img" aria-label="Revolver and folding knife on a wooden table"></div>
    <div class="name">Harlan Mk. V Ridgeline 6.5-300 HRL + Field Pack</div>
    <div class="foot"><span class="left">6d +</span><span class="right">$15,000.00<br>0 Bids</span></div>
  </div>

  <div class="featured-bg" style="left:231px;top:62px"></div>
  <div class="card featured" style="left:239px;top:70px;height:200px">
    <div class="thumb dark" role="img" aria-label="Vintage pistol with ammunition on a dark background"></div>
    <div class="name" style="top:134px">Corwin 1911 Marine MFG 1912 1st contract s/n 3668</div>
  </div>
  <div class="abs" style="left:239px;top:272px;width:181px;height:50px;font-size:12px;color:#555">
    <span class="badge">6d +</span><span class="abs" style="right:22px;top:8px;text-align:right;line-height:18px">$15,000.00<br>0 Bids</span>
  </div>

  <div class="card" style="left:455px;top:70px">
    <div class="thumb cool" role="img" aria-label="Handguns on display at a trade show counter"></div>
    <div class="name">Harlan Mk. V Ridgeline 6.5-300 HRL + Field Pack</div>
    <div class="foot"><span class="left">6d +</span><span class="right">$15,000.00<br>0 Bids</span></div>
  </div>

  <div class="card" style="left:25px;top:372px">
    <div class="thumb warm" role="img" aria-label="Revolver and folding knife on a wooden table"></div>
    <div class="name">Harlan Mk. V Ridgeline 6.5-300 HRL + Field Pack</div>
    <div class="foot"><span class="left">6d +</span><span class="right">$15,000.00<br>0 Bids</span></div>
  </div>
  <div class="card" style="left:239px;top:372px">
    <div class="thumb warm" role="img" aria-label="Revolver and folding knife on a wooden table"></div>
    <div class="name">Harlan Mk. V Ridgeline 6.5-300 HRL + Field Pack</div>
    <div class="foot"><span class="left">6d +</span><span class="right">$15,000.00<br>0 Bids</span></div>
  </div>
  <div class="card" style="left:455px;top:372px">
    <div class="thumb warm" role="img" aria-label="Revolver and folding knife on a wooden table"></div>
    <div class="name">Harlan Mk. V Ridgeline 6.5-300 HRL + Field Pack</div>
    <div class="foot"><span class="left">6d +</span><span class="right">$15,000.00<br>0 Bids</span></div>
  </div>
</section>

<aside>
  <div class="auction" style="top:493px">
    <h4>Trade Expo Auctions</h4>
    <span class="more">More <svg width="5" height="7" viewBox="0 0 5 7"><path d="M0 0l5 3.5L0 7z" fill="#c00d0d"/></svg></span>
    <div class="thumb gold" role="img" aria-label="Hands holding a silver pistol"></div>
    <div class="title">Serial # 1 Outdoor Heritage Day Print</div>
    <div class="sub">1 of 2500 25th Anniversary Print From 1996</div>
    <div class="box"><span class="left">29d +</span><span class="right">$206.00<br>9 Bids</span></div>
  </div>

  <a class="promo" href="#">
    <div class="head">Complete Legal Protection<br>for Armed Self Defense</div>
    <div class="photo" role="img" aria-label="Person practising armed self defense"></div>
    <div class="panel">
      <div class="org">Rearguard<br>Defense</div>
      <div class="seal"></div>
      <div class="join">JOIN TODAY!</div>
      <div class="url">www.rearguarddefense-example.org</div>
    </div>
    <div class="cta">CLICK HERE</div>
  </a>

  <div class="auction" style="top:1135px">
    <h4>Trade Expo Auctions</h4>
    <span class="more">More <svg width="5" height="7" viewBox="0 0 5 7"><path d="M0 0l5 3.5L0 7z" fill="#c00d0d"/></svg></span>
    <div class="thumb steel" role="img" aria-label="Rifles laid out on a table"></div>
    <div class="title">Serial # 1 Outdoor Heritage Day Print</div>
    <div class="sub">1 of 2500 25th Anniversary Print From 1996</div>
    <div class="box"><span class="left">29d +</span><span class="right">$206.00<br>9 Bids</span></div>
  </div>
</aside>

<section class="brands" aria-label="Brands we carry">
  <span><i></i>Kessler</span>
  <span><i></i>Marsh &amp; Tolland</span>
  <span><i></i>Redford</span>
  <span>Westbrook</span>
  <span>Brennan · Stanfield · Vogel</span>
  <span>Corwin</span>
  <span><i></i>Halvard</span>
  <span><i></i>Calderon</span>
  <span><i></i>Bellanti</span>
</section>

<footer class="footer">
  <div class="brand abs">Holloway Arms</div>
  <div class="social" style="left:908px;top:40px"><i></i><i></i><i></i><i></i><i></i><i></i></div>
  <div class="rule"></div>

  <div class="col" style="left:120px">
    <h5 class="strong">Contacts</h5>
    <ul class="contact">
      <li><svg width="14" height="14" viewBox="0 0 24 24" fill="#ddd"><path d="M5 3h4l2 5-2.5 1.5a11 11 0 0 0 6 6L16 13l5 2v4a2 2 0 0 1-2 2A16 16 0 0 1 3 5a2 2 0 0 1 2-2z"/></svg>(800) 555 0147</li>
      <li><svg width="16" height="12" viewBox="0 0 16 12" fill="none" stroke="#ddd" stroke-width="1.4"><rect x="1" y="1" width="14" height="10"/><path d="M1 1l7 6 7-6"/></svg>hello@hollowayarms-example.com</li>
      <li><svg width="12" height="16" viewBox="0 0 20 26" fill="#ddd"><path d="M10 25S2 15 2 9a8 8 0 0 1 16 0c0 6-8 16-8 16z"/></svg><span>48 Larkspur Lane, Fairview,<br>Westmark 3000</span></li>
    </ul>
    <div class="social" style="left:4px;top:200px"><i></i><i></i><i></i><i></i><i></i><i></i></div>
  </div>

  <div class="col" style="left:375px">
    <h5>Latest News</h5>
    <ul class="news">
      <li><b>This is a Audio post type</b><em>January 5,2016</em></li>
      <li><b>This is a Audio post type</b><em>January 5,2016</em></li>
      <li><b>This is a Audio post type</b><em>January 5,2016</em></li>
      <li><b>This is a Audio post type</b><em>January 5,2016</em></li>
    </ul>
  </div>

  <div class="col" style="left:598px">
    <h5 style="margin-bottom:22px">About</h5>
    <ul class="about">
      <li>Home</li><li>Tactical/LE</li><li>Hunting</li><li>Personal Defense</li><li>Cowboy</li><li>Consignments</li><li>Accessories</li><li>About Us</li><li>Find Us</li>
    </ul>
  </div>

  <div class="col" style="left:878px">
    <h5 style="margin-bottom:22px">Quick Contact</h5>
    <div class="field">Your Name</div>
    <div class="field">Your Email</div>
    <div class="field area">Message...</div>
    <div class="submit">SUBMIT</div>
  </div>

  <p class="copyright">© 1999-2017 Holloway Arms, LLC. All rights reserved worldwide.</p>
</footer>

</body>
</html>
```